Tutoring Company Needs a Convincing Brochure

We need a tri-fold brochure for our tutoring/academic enrichment program. TRIM Study House was established in 2000 and is a small business that has thrived in a very competitive and crowded educational market among high profile companies like Velto and Brindle. We offer intimate, affordable academic services for students grades 1-8. At TRIM, our teachers teach! We focus on small group settings, getting to know the families we work with, and engaging teachers that excite students to learn. Our brochure needs to convince parents that we are professional, nurturing and the best choice for their child to reach academic success. We are open minded in the design.

Target Market(s)

parents

Industry/Entity Type

Tutoring

Colors

Designer to choose colors to be used in the design.

Requirements
Must have
• Tri-Fold design, concise, convincing
Nice to have
• Diversity in images

```html
<!DOCTYPE html>
<html lang="en">
<head>
<meta charset="utf-8">
<title>TRIM Study House — Tri-fold Brochure</title>
<link rel="stylesheet" href="https://fonts.googleapis.com/css2?family=Source+Sans+3:wght@400;600;700;800&display=swap">
<style>
:root{
  --orange:#f7941d;
  --blue:#1aa3e8;
  --paper:#f4f4f3;
  --ink:#1d1d1b;
  --white:#ffffff;
  --grey:#d9d9d6;
}
*{box-sizing:border-box;margin:0;padding:0}
html,body{width:1200px;height:802px;overflow:hidden;background:var(--paper)}
body{font-family:"Source Sans 3",Arial,sans-serif;color:var(--ink);position:relative}
.panel{position:absolute;top:0;height:802px}
.panel--about{left:0;width:400px;background:var(--orange)}
.panel--services{left:400px;width:400px;background:var(--paper)}
.panel--pricing{left:800px;width:400px;background:var(--paper)}
.abs{position:absolute}
.about-title{left:34px;top:32px;font-size:25px;font-weight:800;letter-spacing:.3px}
.about-copy{left:32px;width:348px;font-size:13.6px;line-height:17px;text-align:justify}
.book-stack{left:32px;top:362px;width:342px;height:182px;background:linear-gradient(100deg,#6d7fb0 0%,#f2efe6 40%,#ffffff 60%,#8fb46e 100%)}
.update-title{left:0;width:400px;text-align:center;font-weight:800;font-size:20px;line-height:25px}
.update-copy{left:20px;width:360px;text-align:center;font-size:14.5px;line-height:18.5px;top:645px}
.update-link{left:0;width:400px;text-align:center;top:740px;font-size:23px;font-weight:800}
.band{background:var(--blue);color:var(--ink);font-weight:800;text-transform:uppercase;clip-path:polygon(0 0,100% 0,calc(100% - 24px) 100%,0 100%)}
.band--training{left:28px;top:85px;width:300px;height:40px;font-size:15px;padding:12px 0 0 53px}
.training-icon{left:8px;top:73px;width:64px;height:64px}
.presenter{left:195px;top:48px;width:135px;height:42px}
.presenter-name{left:228px;top:66px;font-size:11px;font-weight:800;color:var(--ink)}
.presenter-label{left:262px;top:53px;font-size:6.5px;font-weight:700;letter-spacing:.4px}
.copy{font-size:13.6px;line-height:17px}
.training-copy{left:15px;top:148px;width:370px;text-align:justify}
.learn-more{left:15px;top:250px;color:var(--blue);font-size:13.6px}
.learn-url{left:15px;top:267px;font-size:13.6px}
.milestones{left:230px;top:288px;width:120px;height:108px;background:linear-gradient(160deg,#ffffff 0%,#f6e9c5 35%,#b8d97a 70%,#2bb3a6 100%);transform:rotate(4deg)}
.band--students{left:10px;top:363px;width:360px;height:45px;font-size:15px;line-height:18px;padding:5px 0 0 14px}
.students-copy{left:14px;top:420px;width:372px}
.classroom{left:0;top:505px;width:400px;height:297px;background:linear-gradient(180deg,#f8f8f6 0%,#e4ddd3 45%,#b9a894 75%,#8c8276 100%)}
.report{left:165px;top:45px;width:196px;height:140px;background:linear-gradient(180deg,#ffffff 0%,#eef3f6 50%,#cfe7e0 100%);transform:rotate(3deg);border:1px solid var(--grey)}
.band--test{left:20px;top:163px;width:358px;height:46px;font-size:15px;line-height:18px;padding:6px 0 0 13px}
.test-copy{left:23px;top:218px;width:362px;text-align:justify}
.group-box{left:18px;top:322px;width:366px;height:166px;background:var(--blue)}
.group-title{left:46px;top:311px;width:318px;height:30px;background:var(--white);border:1.5px solid var(--ink);font-weight:800;font-size:14.5px;text-align:center;padding-top:5px}
.group-subjects{left:30px;top:364px;width:120px;color:var(--white);font-size:11px;line-height:13.5px}
.group-divider{left:143px;top:360px;width:1px;height:88px;background:var(--white)}
.group-prices{left:153px;top:364px;width:230px;color:var(--white);font-size:11px;line-height:13.5px}
.group-prices b{font-weight:700}
.row{display:flex;justify-content:space-between;width:205px}
.homework{left:30px;top:458px;color:var(--white);font-weight:700;font-size:11px}
.addmore-title{left:32px;top:498px;font-weight:800;font-size:14.5px}
.addmore-list{left:42px;top:521px;font-size:10.8px;line-height:15.3px;list-style:none}
.tutor-title{left:30px;top:645px;width:380px;text-align:center;font-weight:800;font-size:15px;line-height:18px}
.rate{font-size:11px;display:flex;align-items:center}
.rate span.price{background:var(--blue);padding:1px 3px;margin-left:3px}
.rate span.dots{letter-spacing:-.5px}
.bottom-rule{left:0;top:798px;width:400px;height:4px;background:var(--blue)}
</style>
</head>
<body>

<section class="panel panel--about">
  <h1 class="abs about-title">ABOUT US</h1>
  <p class="abs about-copy" style="top:75px">At TRIM, we teach. TRIM’s iLevel diagnostic and level curriculam guides out teachers to target exactly what your child needs to learn. Our teachers engage, instruct and excite your child to understand, enjoy and succeed in acadamics.</p>
  <p class="abs about-copy" style="top:179px">Each student’s lesson plan is personalized to meet their academic need. We strengthen foundational skills and ensure students are challenged.</p>
  <p class="abs about-copy" style="top:253px">TRIM develops independent learners by instilling positive attitudes towards learning, building academic confidence and teaching skills needed for your chils to become an extraordinary student.</p>
  <div class="abs book-stack" role="img" aria-label="Fanned stack of Level mathematics workbooks and lesson pages"></div>
  <p class="abs update-title" style="top:578px">* UPADTED 2017 *</p>
  <p class="abs update-title" style="top:603px">REWRITTEN FOR THE COMMON CORE</p>
  <p class="abs update-copy">Check it out, curriculam older than 2015 does not meet new standards.<br>Visit link below to see how TRIM’s LEVEL meets all Expectatons</p>
  <p class="abs update-link">trimstudy.link/LEVEL</p>
</section>

<section class="panel panel--services">
  <svg class="abs presenter" viewBox="0 0 135 42" aria-hidden="true">
    <polygon points="18,2 133,2 117,40 2,40" fill="#fff" stroke="#f7941d" stroke-width="3"/>
  </svg>
  <span class="abs presenter-label">PRESENTED BY</span>
  <span class="abs presenter-name">ClassPro Tutors</span>

  <div class="abs band band--training">One on one training</div>
  <svg class="abs training-icon" viewBox="0 0 64 64" aria-hidden="true">
    <circle cx="32" cy="32" r="32" fill="#f7941d"/>
    <rect x="22" y="16" width="26" height="18" fill="none" stroke="#fff" stroke-width="2"/>
    <line x1="26" y1="22" x2="44" y2="22" stroke="#fff" stroke-width="1.6"/>
    <line x1="26" y1="27" x2="40" y2="27" stroke="#fff" stroke-width="1.6"/>
    <circle cx="20" cy="38" r="3.5" fill="#fff"/>
    <path d="M14 50 v-6 a6 6 0 0 1 12 0 v6 z" fill="#fff"/>
    <line x1="24" y1="42" x2="30" y2="35" stroke="#fff" stroke-width="2"/>
  </svg>
  <p class="abs copy training-copy">Setup private tutoring with a credentialed, classroom teacher. Teachers are up-to-date with current methodologies, acadamic content and standards.<br>Teachers understand grade-level requirements resulting in targeted instruction for your child.</p>
  <p class="abs learn-more">Learn More:</p>
  <p class="abs learn-url">www.classprotutors.com</p>

  <div class="abs milestones" role="img" aria-label="TRIM Mastery Milestones checklist sheets"></div>
  <div class="abs band band--students">TRIM creates<br>extraordinary students</div>
  <p class="abs copy students-copy">Our Mastery milestones help Develop independent learners with guidelines focused on students behaviour &amp; Work Ethic, Common Core Foundational concepts, and study skills habits.</p>
  <div class="abs classroom" role="img" aria-label="Smiling teacher leaning over a table of young students in a classroom"></div>
</section>

<section class="panel panel--pricing">
  <div class="abs report" role="img" aria-label="Sample diagnostic performance report with bar charts"></div>
  <div class="abs band band--test">We test for<br>success 3 times per year</div>
  <p class="abs copy test-copy">Our academic diagnostic uses adaptive technolgy, similar to the NSAT, to pinpoint exact areas of needed improvement across multiple a personalized lesson plan.</p>

  <div class="abs group-box"></div>
  <div class="abs group-title">SMALL GROUP TUTORING &amp; ENRICHMENT</div>
  <p class="abs group-subjects">Choose what to study:<br>TRIM’s Level Math<br>TRIM’s Level Reading<br>TRIM’s Level Writing<br>/Grammar</p>
  <div class="abs group-divider"></div>
  <div class="abs group-prices">
    <b>Pricing ( $100 one-time registration fee )</b>
    <div class="row"><span>One subject (1hr/wk)............</span><span>$ 150 Per Month</span></div>
    <div class="row"><span>Two Subjects (2 hrs/wk).......</span><span>$ 275 Per Month</span></div>
    <div class="row"><span>Three Subjects (3hrs/wk)......</span><span>$ 375 Per Month</span></div>
    <div class="row"><span>Four Subjects (4hrs/wk) .......</span><span>$ 450 Per Month</span></div>
    above prices for autoplay, +$20 for non-autopay
  </div>
  <p class="abs homework">School Home work Help includes all subjects</p>

  <h2 class="abs addmore-title">ADD MORE, LEARN MORE</h2>
  <ul class="abs addmore-list">
    <li>+ add 1/2 hr per wk for $50 Per Month</li>
    <li>+ add 1 hr per wk of School Homework Help for $75 Per Month</li>
    <li>+ add TRIM Homework for $20 per mont per subject</li>
    <li>+ add Online Academic Lessons for $10 per month</li>
  </ul>

  <h2 class="abs tutor-title">1 - ON -1 TUTORING WITH A CREDENTIALED,<br>CLASSROOM TEACHER</h2>
  <div class="abs rate" style="left:27px;top:693px"><span>Grade k-5 </span><span class="dots">...............</span><span class="price">$70 Per Hour</span></div>
  <div class="abs rate" style="left:27px;top:712px"><span>Grade 6-8 </span><span class="dots">...............</span><span class="price">$80 Per Hour</span></div>
  <div class="abs rate" style="left:198px;top:693px"><span>Grade 9-12 </span><span class="dots">...............</span><span class="price">$90 Per Hour</span></div>
  <div class="abs rate" style="left:198px;top:714px"><span>Adv. Prep, Test Prep </span><span class="dots">......</span><span class="price">$110 Per Hour</span></div>
  <div class="abs bottom-rule"></div>
</section>

</body>
</html>
```